interior designer/stylist looking for a letter press business card to reflect the stylish work

Hello Designers,
I need a business card design for an company called Harrow Fenwick Interior Design. I'm aiming at the high end residential and private client market in London providing sleek simple interiors. I'd like my business card to be snapboard worthy and expensive looking, i want people to clip it and for it to have a sought after look, and want prospective customers to hire me as their interior designer as my card is so beautiful.
I love letter press design. I also like the use of colour/foil on the edge.
Colour combos & general things I like -
Black and White
Navy Blue and Gold
Neutral colours (muted palette of greys whites navys beiges)
White Marble & brass
Vosque (fashion designer)
....also open to other suggestions....
Please dont take the pink in the attached photos too literally. i'd like the card to look more masculine than feminine.
I'd like Harrow Fenwick on one side in one font, with interior design underneath so one word will make the statement....... unless anyone has any other ideas, open to suggestions.
I'd like a really simple font and for the whole card to look very graphic.
my details -
Marta Quibbley
Interior Designer & Stylist
email marta@harrowfenwickinteriors.co.uk
phone +447700184396
website wwww.harrowfenwickinteriors.co.uk
GO GO GO!! EXCITED TO SEE THE OUTCOME!!
x L
High End Residential and private clients
Business
Contact Information for Business Card
Harrow Fenwick Interior Design & Styling
Marta Quibbley
phone +447700184396

```html
<!DOCTYPE html>
<html lang="en">
<head>
<meta charset="utf-8">
<title>Harrow Fenwick Interior Design — Business Card</title>
<link rel="stylesheet" href="https://fonts.googleapis.com/css2?family=Jost:wght@300;400&display=swap">
<style>
  :root {
    --backdrop: #ececec;
    --card: #ffffff;
    --card-edge: #d9d9d9;
    --ink: #6a6a6a;
    --ink-soft: #8a8a8a;
  }
  * { margin: 0; padding: 0; box-sizing: border-box; }
  html, body {
    width: 1200px;
    height: 716px;
    overflow: hidden;
    background: var(--backdrop);
  }
  body {
    position: relative;
    font-family: "Jost", "Futura", sans-serif;
    font-weight: 300;
    color: var(--ink);
  }
  .card {
    position: absolute;
    width: 520px;
    height: 300px;
    background: var(--card);
    border: 1px solid var(--card-edge);
    box-shadow: 0 0 0 3px #f4f4f4, 0 0 0 4px var(--card-edge);
    display: flex;
    align-items: center;
    justify-content: center;
  }
  .card--contact { left: 70px; top: 90px; }
  .card--brand { left: 610px; top: 326px; }

  .contact-block { display: inline-block; }
  .contact-name {
    font-size: 33px;
    letter-spacing: 0.08em;
    text-transform: uppercase;
    line-height: 1;
  }
  .contact-role {
    margin-top: 8px;
    font-size: 11px;
    letter-spacing: 0.38em;
    text-transform: uppercase;
    color: var(--ink-soft);
  }
  .contact-details {
    margin-top: 22px;
    text-align: right;
    list-style: none;
    font-size: 11.5px;
    letter-spacing: 0.02em;
    text-transform: uppercase;
    line-height: 1.85;
  }
  .contact-details .contact-web { font-size: 13px; }

  .brand-block { display: inline-block; }
  .brand-name {
    font-size: 44px;
    letter-spacing: 0.07em;
    text-transform: uppercase;
    line-height: 1;
  }
  .brand-tagline {
    margin-top: 6px;
    font-size: 13px;
    letter-spacing: 0.38em;
    text-transform: uppercase;
    color: var(--ink-soft);
  }
</style>
</head>
<body>
  <section class="card card--contact">
    <div class="contact-block">
      <h1 class="contact-name">Marta Quibbley</h1>
      <p class="contact-role">Interior Designer &amp; Stylist</p>
      <ul class="contact-details">
        <li class="contact-email">marta@harrowfenwickinteriors.co.uk</li>
        <li class="contact-phone">+447700184396</li>
        <li class="contact-web">www.harrowfenwickinteriors.co.uk</li>
      </ul>
    </div>
  </section>

  <section class="card card--brand">
    <div class="brand-block">
      <h2 class="brand-name">Harrow Fenwick</h2>
      <p class="brand-tagline">Interior Design</p>
    </div>
  </section>
</body>
</html>
```